Web Page Design for a Website that Provides Tutoring

I am looking to create an online tutoring website. The website will allow parents or students to contact tutors with a view to instructing them to tutor themselves or their children.

The name of the website is LendYourLessons.

This brief is to create the design for one of the web pages for this web site. I am hoping the same designer will be available to design other pages.

The page I want designed is one of the more complex and I have attached the design as an excel spreadsheet. The web page needs to include all the items on this page but if you want to change the positioning of the items then Im fine with that.

I recently had two logos created for this website. My favourite is the one with a mortar board but im not sure I like the colours. I have attached both of these logos and you can use either of them, change the colours or create something different. I just want a design pleasing to the eye. If the logo is changed I would like that in a seperate file.

So can you please submit designs for this page. I have attached the two logos which you can use, change or if you feel you have a better idea then you can use that.

On the spreadsheet the Send Message, Favourite etc are buttons.

Target Market(s)

People who want to better themselves.
Possible middle class to upper class.

Industry/Entity Type

Tutoring

Number of Pages Required

1 page

Requirements
Must have
• The designs must have alot of the information attached in the spreadsheet.

```html
<!DOCTYPE html>
<html lang="en">
<head>
<meta charset="utf-8">
<title>LendYourLessons – Tutor Profile</title>
<link href="https://fonts.googleapis.com/css2?family=Catamaran:wght@400;500;600;700&family=Roboto:wght@400&display=swap" rel="stylesheet">
<style>
:root{
  --ink:#222;
  --muted:#8a8f96;
  --faint:#b2b6bb;
  --line:#d8dadd;
  --header-bg:#f1f4f8;
  --blue:#5ea7d2;
  --teal:#24a896;
  --orange:#fd6641;
  --star:#f7b21a;
  --star-off:#b9bec4;
  --cell:#e6e6e6;
  --cell-head:#a9a9a9;
  --cell-head-dark:#878787;
  --review-bg:#f0f3f6;
  --footer-bg:#3a3a3a;
  --white:#fff;
}
*{box-sizing:border-box;margin:0;padding:0}
html,body{width:893px;height:1200px;overflow:hidden;background:var(--white)}
body{position:relative;font-family:'Catamaran',sans-serif;color:var(--ink);font-size:11px}
.abs{position:absolute}

/* header */
.site-header{position:absolute;left:0;top:0;width:893px;height:102px;background:var(--header-bg)}
.brand{position:absolute;left:78px;top:58px;display:flex;align-items:center;gap:6px}
.brand-mark{width:14px;height:14px;background:var(--blue)}
.brand-name{font-size:17px;font-weight:600;color:var(--blue)}
.search-label{left:257px;top:36px;color:var(--faint);font-size:11px}
.search-box{left:299px;top:28px;width:335px;height:30px;border:1px solid #c8cbd0;border-radius:3px;background:var(--white);display:flex;align-items:center;padding-left:10px;gap:6px;font-size:11px;font-weight:600}
.search-btn{left:642px;top:28px;width:32px;height:31px;background:var(--orange);border-radius:3px;display:flex;align-items:center;justify-content:center}
.sign-in{left:700px;top:36px;font-size:11px;font-weight:600}
.sign-up{left:753px;top:28px;width:66px;height:31px;border-radius:16px;background:var(--blue);color:var(--white);font-size:11px;font-weight:600;display:flex;align-items:center;justify-content:center}
.main-nav{left:299px;top:73px;display:flex;gap:0;font-size:11px;font-weight:600}
.main-nav span{margin-right:20px;padding-bottom:2px}
.main-nav .active{color:var(--ink);border-bottom:2px solid var(--blue)}

/* profile */
.rule{position:absolute;height:1px;background:var(--line)}
.avatar{left:167px;top:143px;width:70px;height:70px;border-radius:50%;background:radial-gradient(circle at 50% 40%,#8a6f5e,#3b3430)}
.profile-text{left:248px;top:138px;line-height:16px;font-size:11.5px;color:#444}
.profile-text .name{font-size:14px;color:var(--ink);font-weight:500;margin-bottom:1px}
.divider-v{left:622px;top:138px;width:1px;height:84px;background:var(--line)}
.stats{left:634px;top:134px;font-size:11px;font-weight:600;line-height:18px}
.stats .row{display:flex;align-items:center;height:17.5px}
.stats .label{width:64px}
.stars{display:flex;gap:2px}

/* details box */
.details{left:157px;top:243px;width:613px;height:218px;border:2px solid #333;border-radius:3px}
.details .meta{position:absolute;left:15px;top:14px;font-size:10px;font-weight:500;line-height:15px}
.details .subj{position:absolute;left:15px;top:57px;font-size:10.5px;font-weight:600}
.rates{position:absolute;left:15px;top:78px;width:582px;border-collapse:collapse;font-size:10px;font-weight:500}
.rates th,.rates td{height:23px;border-top:1px solid var(--line);border-left:1px solid var(--line);text-align:center;font-weight:500}
.rates tr>*:first-child{border-left:none;text-align:left;width:99px}
.rates tr:last-child td{border-bottom:1px solid var(--line)}
.rates th:last-child{text-align:left;padding-left:10px}
.rates .spacer td{height:26px;border-left:none}
.actions{position:absolute;left:15px;top:184px;display:flex;gap:7px}
.btn{height:23px;border-radius:2px;color:var(--white);font-size:9.5px;font-weight:600;display:flex;align-items:center;gap:8px;padding:0 8px}
.btn-fav{background:var(--orange);width:86px}
.btn-msg{background:var(--blue);width:103px}
.btn-rev{background:var(--teal);width:103px}

/* availability */
.section-title{font-size:17px;font-weight:600;color:var(--teal)}
.availability{left:153px;top:507px;display:grid;grid-template-columns:77px repeat(7,76px);grid-auto-rows:23px;column-gap:2px;row-gap:3px}
.availability .head{background:var(--cell-head);color:#333;font-family:'Roboto',sans-serif;font-size:10.5px;display:flex;align-items:center;justify-content:center}
.availability .head.dark{background:var(--cell-head-dark)}
.availability .slot{background:var(--cell)}
.availability .time{background:var(--cell);display:flex;align-items:center;justify-content:center;font-size:12px;font-family:'Roboto',sans-serif}
.slot.taken{background:var(--teal)}
.slot.reserved{background:var(--blue)}
.slot.no{background:var(--orange)}
.legend{left:235px;top:683px;display:flex;gap:16px;font-size:12.5px;font-weight:500;align-items:center}
.legend span{display:flex;align-items:center;gap:6px}
.legend i{display:inline-block;width:10px;height:10px}

/* reviews */
.reviews{left:155px;top:751px;width:614px;height:262px;background:var(--review-bg);padding:0 17px 0 22px}
.review{height:88px;padding-top:12px;border-bottom:1px solid var(--line);position:relative}
.review:last-child{border-bottom:none}
.review .who{font-size:10px;font-weight:600;display:flex;gap:8px;align-items:center}
.review .who small{color:#d7b44b;font-size:8px;letter-spacing:1px}
.review .when{position:absolute;right:0;top:13px;font-size:8.5px;color:var(--faint)}
.review p{font-size:9.8px;color:var(--muted);line-height:15px;margin-top:3px}
.review .foot{display:flex;justify-content:space-between;margin-top:5px;font-size:10px}
.review .answers{color:var(--blue)}
.review .helpful{font-size:8.5px;color:var(--faint)}
.review .helpful b{font-size:10.5px;font-weight:600;margin-left:8px}
.yes{color:var(--teal)} .no{color:var(--orange)} .cnt{color:var(--ink)}

/* footer */
.site-footer{position:absolute;left:0;top:1050px;width:893px;height:125px;background:var(--footer-bg);color:var(--white)}
.foot-nav{position:absolute;left:286px;top:26px;display:flex;font-size:10.5px;font-weight:600}
.foot-nav span{margin-right:16px}
.socials{position:absolute;left:362px;top:57px;display:flex;gap:13px}
.socials i{width:24px;height:24px;border-radius:50%;display:block}
.copyright{position:absolute;left:0;width:893px;top:103px;text-align:center;font-size:8px;color:#ccc}
</style>
</head>
<body>

<header class="site-header">
  <div class="brand"><span class="brand-mark"></span><span class="brand-name">LendYourLessons</span></div>
  <span class="abs search-label">Search</span>
  <div class="abs search-box">
    <svg width="10" height="10" viewBox="0 0 10 10"><circle cx="4" cy="4" r="3" fill="none" stroke="#999" stroke-width="1.2"/><line x1="6.3" y1="6.3" x2="9" y2="9" stroke="#999" stroke-width="1.2"/></svg>
    Flat
  </div>
  <div class="abs search-btn"><svg width="13" height="13" viewBox="0 0 10 10"><circle cx="4" cy="4" r="3" fill="none" stroke="#fff" stroke-width="1.3"/><line x1="6.3" y1="6.3" x2="9" y2="9" stroke="#fff" stroke-width="1.4"/></svg></div>
  <span class="abs sign-in">Sign in</span>
  <div class="abs sign-up">Sign up</div>
  <nav class="abs main-nav"><span>Home</span><span class="active">Search</span><span>Student</span><span>Tutor</span><span style="margin-right:14px">About Us</span><span>Contact Us</span></nav>
</header>

<div class="rule" style="left:156px;top:128px;width:614px"></div>
<div class="abs avatar" role="img" aria-label="Tutor portrait photo"></div>
<div class="abs profile-text">
  <div class="name">Tom Weller</div>
  <div>Hi my name is Tom I am a .....Lorem ipsum is mostly a part of a ...</div>
  <div>Male, 29 Years</div>
  <div>5 Years of Teaching Experience</div>
  <div>Bachelor's Degree in Education</div>
</div>
<div class="abs divider-v"></div>
<div class="abs stats">
  <div class="row"><span class="label">Review:</span>
    <svg width="78" height="13" viewBox="0 0 78 13"><g id="s"><polygon points="6,0.5 7.6,4.5 11.8,4.6 8.5,7.2 9.7,11.6 6,9.1 2.3,11.6 3.5,7.2 0.2,4.6 4.4,4.5" fill="#f7b21a"/></g><use href="#s" x="16"/><use href="#s" x="32"/><use href="#s" x="48"/><polygon transform="translate(64 0)" points="6,0.5 7.6,4.5 11.8,4.6 8.5,7.2 9.7,11.6 6,9.1 2.3,11.6 3.5,7.2 0.2,4.6 4.4,4.5" fill="#b9bec4"/></svg></div>
  <div class="row"><span class="label">Reliability:</span>
    <svg width="78" height="13" viewBox="0 0 78 13"><use href="#s"/><use href="#s" x="16"/><use href="#s" x="32"/><use href="#s" x="48"/><polygon transform="translate(64 0)" points="6,0.5 7.6,4.5 11.8,4.6 8.5,7.2 9.7,11.6 6,9.1 2.3,11.6 3.5,7.2 0.2,4.6 4.4,4.5" fill="#b9bec4"/></svg></div>
  <div class="row"><span class="label">Punctuality:</span>
    <svg width="78" height="13" viewBox="0 0 78 13"><use href="#s"/><use href="#s" x="16"/><use href="#s" x="32"/><use href="#s" x="48"/><polygon transform="translate(64 0)" points="6,0.5 7.6,4.5 11.8,4.6 8.5,7.2 9.7,11.6 6,9.1 2.3,11.6 3.5,7.2 0.2,4.6 4.4,4.5" fill="#b9bec4"/></svg></div>
  <div class="row" style="margin-top:3px">Member Since: 06/01/2015</div>
  <div class="row">Last Logged In:&nbsp; 05/11/2016</div>
</div>
<div class="rule" style="left:156px;top:230px;width:614px"></div>

<section class="abs details">
  <div class="meta">* Tutoring Type: In personal only<br>* Willing To Travel</div>
  <div class="subj">Subjects Taught</div>
  <table class="rates">
    <tr><th></th><th>Primary</th><th>Secondary</th><th>GCSE</th><th>A-LEVEL</th><th>University</th><th>Adult Learner</th></tr>
    <tr><td>Biology</td><td>$20</td><td></td><td>$20</td><td></td><td></td><td></td></tr>
    <tr><td>Chemistry</td><td>$25</td><td></td><td></td><td>$30</td><td></td><td></td></tr>
    <tr class="spacer"><td colspan="7"></td></tr>
  </table>
  <div class="actions">
    <div class="btn btn-fav"><svg width="14" height="12" viewBox="0 0 14 12"><path d="M7 11.5 1.3 6A3.2 3.2 0 0 1 7 1.8 3.2 3.2 0 0 1 12.7 6Z" fill="#fff"/></svg>Favour Tutor</div>
    <div class="btn btn-msg"><svg width="14" height="10" viewBox="0 0 14 10"><rect x="0.7" y="0.7" width="12.6" height="8.6" rx="1" fill="none" stroke="#fff" stroke-width="1.2"/><path d="M1 1 7 6 13 1" fill="none" stroke="#fff" stroke-width="1.2"/></svg>Send Message</div>
    <div class="btn btn-rev"><svg width="16" height="14" viewBox="0 0 16 14"><path d="M1 1h14v9H6l-3 3v-3H1Z" fill="none" stroke="#fff" stroke-width="1.3"/><line x1="4" y1="4" x2="12" y2="4" stroke="#fff"/><line x1="4" y1="7" x2="10" y2="7" stroke="#fff"/></svg>Write Review</div>
  </div>
</section>

<h2 class="abs section-title" style="left:158px;top:484px">Availability</h2>
<div class="abs availability">
  <div></div><div class="head">MON</div><div class="head">TUE</div><div class="head">WED</div><div class="head">THR</div><div class="head">FRI</div><div class="head dark">SUN</div><div class="head dark">SAT</div>
  <div class="time">7 - 8</div><div class="slot reserved"></div><div class="slot"></div><div class="slot"></div><div class="slot"></div><div class="slot"></div><div class="slot"></div><div class="slot"></div>
  <div class="time">8 - 9</div><div class="slot"></div><div class="slot"></div><div class="slot reserved"></div><div class="slot taken"></div><div class="slot"></div><div class="slot"></div><div class="slot no"></div>
  <div class="time">4 - 5</div><div class="slot"></div><div class="slot"></div><div class="slot"></div><div class="slot"></div><div class="slot taken"></div><div class="slot"></div><div class="slot no"></div>
  <div class="time">5 - 6</div><div class="slot taken"></div><div class="slot"></div><div class="slot"></div><div class="slot"></div><div class="slot"></div><div class="slot"></div><div class="slot"></div>
  <div class="time">7 - 8</div><div class="slot"></div><div class="slot reserved"></div><div class="slot reserved"></div><div class="slot"></div><div class="slot"></div><div class="slot reserved"></div><div class="slot"></div>
</div>
<div class="abs legend">
  <span><i style="background:var(--cell)"></i>Available</span>
  <span style="gap:2px"><i style="background:var(--teal)"></i>Taken</span>
  <span style="gap:3px"><i style="background:var(--blue)"></i>Reserved</span>
  <span><i style="background:var(--orange)"></i>No</span>
</div>
<div class="rule" style="left:155px;top:707px;width:614px"></div>

<h2 class="abs section-title" style="left:158px;top:725px">Reviews</h2>
<section class="abs reviews">
  <article class="review">
    <div class="who">Owen Marlow <small>★★★★★</small></div>
    <span class="when">◷ Just now</span>
    <p>He was justified by the event; for the footpath soon after appeared a little wider and more worn, and the tinkle of a small bell gave the knight to understand that he was in the vicinity of some chapel or hermitage.</p>
    <div class="foot"><span class="answers">3 answers</span><span class="helpful">Was this review helpful? <b class="yes">YES <span class="cnt">(2)</span></b> <b class="no">NO <span class="cnt">(1)</span></b></span></div>
  </article>
  <article class="review">
    <div class="who">Felix Harrowby <small>★★★★★</small></div>
    <span class="when">◷ 5 august</span>
    <p>Alice wondered a little at this, but she was too much in awe of the Queen to disbelieve it. 'I'll try it when I go home,' she thought to herself, 'the next time I'm a little late for dinner.'</p>
    <div class="foot"><span class="answers">1 answer</span><span class="helpful">Was this review helpful? <b class="yes">YES <span class="cnt">(2)</span></b> <b class="no">NO <span class="cnt">(1)</span></b></span></div>
  </article>
  <article class="review">
    <div class="who">Leon Castell <small>★★★★</small></div>
    <span class="when">◷ 6 august</span>
    <p>Now the races of these two have been for some ages utterly extinct, and besides to discourse any further of them would not be at all to my purpose.</p>
    <div class="foot"><span class="answers">0 answers</span><span class="helpful">Was this review helpful? <b class="yes">YES <span class="cnt">(5)</span></b> <b class="no">NO <span class="cnt">(0)</span></b></span></div>
  </article>
</section>

<footer class="site-footer">
  <nav class="foot-nav"><span style="margin-right:20px">Home</span><span style="margin-right:21px">Search</span><span style="margin-right:21px">Student</span><span>Tutor</span><span style="margin-right:15px">About Us</span><span>Contact Us</span></nav>
  <div class="socials">
    <i style="background:#3b5a9a"></i><i style="background:#2aa3dd"></i><i style="background:#e94b8f"></i><i style="background:#1aa0b5"></i><i style="background:#e2504a"></i>
  </div>
  <div class="copyright">©LENDYOURLESSONS 2016 – All Right Reserved</div>
</footer>

</body>
</html>
```